Business Card Design Project

I have just chosen a logo and would now like this designed onto a business card for my hair salon. I would like it to be classy not to busy and have a wow factor when people look at them
Has to Include on card:
Logo Design
And business details below
Kellie-ann Drummond (owner)
0482 736 219
Rdw@vomblet.com.au
71 Willowmere Rise Corvin Cove
Logo is now attached please provide designs
Hair

```html
<!DOCTYPE html>
<html lang="en">
<head>
<meta charset="utf-8">
<title>Shear Grace Hair Salon – Business Cards</title>
<link rel="stylesheet" href="https://fonts.googleapis.com/css2?family=Questrial&family=Dancing+Script:wght@500&family=Josefin+Sans:wght@400;600&display=swap">
<style>
  :root {
    --page: #ffffff;
    --card: #f8f8f8;
    --card-edge: #e6e6e6;
    --silver: #d3d3d3;
    --gold-light: #ecd3a6;
    --gold-deep: #c79a63;
    --label-bg: #f1f1f1;
    --label-text: #707070;
    --tan: #a87c52;
    --brown: #7a3f1c;
  }
  * { margin: 0; padding: 0; box-sizing: border-box; }
  html, body { width: 1200px; height: 675px; overflow: hidden; background: var(--page); }
  .canvas { position: relative; width: 1200px; height: 675px; }

  .card {
    position: absolute;
    background: var(--card);
    border: 1px solid var(--card-edge);
    overflow: hidden;
  }
  .card--pattern-front { left: 44px; top: 33px; width: 404px; height: 235px; border-radius: 6px; }
  .card--logo-front    { left: 551px; top: 31px; width: 402px; height: 235px; }
  .card--script-back   { left: 44px; top: 323px; width: 404px; height: 236px; border-radius: 6px; }
  .card--salon-back    { left: 553px; top: 323px; width: 395px; height: 234px; }

  /* Gold dotted front */
  .pattern-field {
    position: absolute; left: 23px; top: 19px; width: 368px; height: 195px;
    background: radial-gradient(circle at 35% 55%, var(--gold-light) 0%, var(--gold-deep) 45%, var(--silver) 100%);
  }
  .name-label {
    position: absolute; left: 88px; top: 85px; width: 237px; height: 59px;
    background: var(--label-bg);
    text-align: center;
  }
  .name-label__text {
    display: block; margin-top: 13px;
    font-family: "Questrial", sans-serif; font-size: 15px; color: var(--label-text); letter-spacing: 0.3px;
  }
  .name-label__rule {
    position: absolute; left: 14px; right: 14px; top: 37px; height: 1px; background: #9a9a9a;
  }

  /* Logo front */
  .brand-mark {
    position: absolute; left: 0; right: 0; top: 96px;
    display: flex; align-items: center; justify-content: center; gap: 12px;
  }
  .brand-mark__dot { width: 14px; height: 14px; border-radius: 50%; background: var(--brown); }
  .brand-mark__name {
    font-family: "Josefin Sans", sans-serif; font-weight: 600; font-size: 40px;
    color: var(--brown); letter-spacing: 4px; line-height: 1;
  }

  /* Script back */
  .script-details {
    position: absolute; left: 0; right: 0; top: 64px; text-align: center;
    font-family: "Dancing Script", cursive; color: var(--tan);
  }
  .script-details__name { font-size: 21px; margin-bottom: 14px; }
  .script-details__line { font-size: 20px; line-height: 28px; }

  /* Salon back */
  .salon-band {
    position: absolute; left: 82px; top: 60px; width: 248px; height: 19px;
    background: var(--brown); color: #fff; text-align: center;
    font-family: "Josefin Sans", sans-serif; font-size: 13px; line-height: 20px; letter-spacing: 0.3px;
  }
  .salon-details {
    position: absolute; left: 82px; width: 248px; top: 88px; text-align: center;
    font-family: "Josefin Sans", sans-serif; color: var(--brown); font-size: 9px; line-height: 12px;
  }
  .salon-details__name { margin-bottom: 10px; }
  .salon-rule {
    position: absolute; left: 82px; top: 154px; width: 248px; height: 4px; background: var(--brown);
  }
</style>
</head>
<body>
<main class="canvas">

  <section class="card card--pattern-front">
    <div class="pattern-field" role="img" aria-label="Scattered metallic gold circles on a soft silver background"></div>
    <div class="name-label">
      <span class="name-label__text">Kellie-ann Drummond</span>
      <span class="name-label__rule"></span>
    </div>
  </section>

  <section class="card card--logo-front">
    <div class="brand-mark">
      <span class="brand-mark__dot"></span>
      <span class="brand-mark__name">SHEAR GRACE</span>
    </div>
  </section>

  <section class="card card--script-back">
    <div class="script-details">
      <p class="script-details__name">Kellie-ann Drummond</p>
      <p class="script-details__line">0482 736 219</p>
      <p class="script-details__line">Rdw@vomblet.com.au</p>
      <p class="script-details__line">71 Willowmere Rise Corvin Cove</p>
    </div>
  </section>

  <section class="card card--salon-back">
    <div class="salon-band">SHEAR GRACE HAIR SALON</div>
    <div class="salon-details">
      <p class="salon-details__name">Kellie-ann Drummond</p>
      <p>0482 736 219</p>
      <p>Rdw@vomblet.com.au</p>
      <p>71 Willowmere Rise Corvin Cove</p>
    </div>
    <div class="salon-rule"></div>
  </section>

</main>
</body>
</html>
```